Providing Back Office Solutions to Financial Advisors and Attorney Needs a Business Card Design

Need a Business Card Design that speaks to Financial Advisor and Attorneys. Some of the word that come to mind is Clean/Simple & Futuristic.

Industry/Entity Type

Business

```html
<!DOCTYPE html>
<html lang="en">
<head>
<meta charset="utf-8">
<title>Norvane Business Card</title>
<link href="https://fonts.googleapis.com/css2?family=Saira+Condensed:wght@400;500&display=swap" rel="stylesheet">
<style>
  :root {
    --page-bg: #eceeed;
    --card-blue: #0a8ed5;
    --ink-white: #ffffff;
    --tagline-blue: #5cb8ec;
  }
  html, body {
    margin: 0;
    padding: 0;
    width: 1200px;
    height: 1200px;
    overflow: hidden;
    background: var(--page-bg);
  }
  .card {
    position: absolute;
    left: 340px;
    top: 145px;
    width: 520px;
    height: 910px;
    background: var(--card-blue);
    font-family: "Saira Condensed", "Arial Narrow", sans-serif;
    color: var(--ink-white);
    overflow: hidden;
  }
  .brand-mark {
    position: absolute;
    left: 222px;
    top: 250px;
    width: 76px;
    height: 76px;
    background: var(--ink-white);
  }
  .brand-name {
    position: absolute;
    left: 0;
    width: 520px;
    top: 372px;
    margin: 0;
    text-align: center;
    font-weight: 500;
    font-size: 104px;
    line-height: 1;
    letter-spacing: 6px;
  }
  .tagline {
    position: absolute;
    left: 0;
    width: 520px;
    top: 490px;
    margin: 0;
    text-align: center;
    font-weight: 400;
    font-size: 36px;
    letter-spacing: 1px;
    color: var(--tagline-blue);
    line-height: 1;
  }
  .contact {
    position: absolute;
    left: 145px;
    top: 568px;
    margin: 0;
    font-style: normal;
    font-weight: 400;
    font-size: 30px;
    line-height: 31px;
  }
  .contact .gap { display: block; height: 9px; }
  .rule {
    position: absolute;
    left: 145px;
    top: 812px;
    width: 226px;
    height: 7px;
    background: var(--ink-white);
  }
</style>
</head>
<body>
  <div class="card">
    <div class="brand-mark" aria-hidden="true"></div>
    <h1 class="brand-name">NORVANE</h1>
    <p class="tagline">BACK OFFICE SOLUTIONS</p>
    <address class="contact">
      Dale Corwin - GM<br>
      2718 Birch Lane<br>
      Lakeport, FL 32100<span class="gap"></span>
      555-214-7730<span class="gap"></span>
      555-386-0142<br>
      corwin@norvane.com
    </address>
    <div class="rule"></div>
  </div>
</body>
</html>
```